Ranked amongst the Best Colleges and Programs

the size of the ad is Full Page, with bleed*
8”x 10.75" plus 0.25" bleed'
you have two choices for the tagline .. please chose what ever you think will allow you to make a better ad.
The instructions on the brief are in red
I am looking for a hight quality modern ad to place in local weekly publications that will stand out .
I would like a ad that people will look at and say i would like to see what this ad is all about.
I apprecate creative work.
the ad should not be very crowded and the text should be able to be read.
if you decide to use people in the ad .. (you don't have to ) then it should be a male dressed in white shirt in and sports jacket.. or if you would like you can use a vector and then use male or female people.
please leave one inch on the bottom for the footer

Target Market(s)

potential middle class students from 23-35 years of age

Industry/Entity Type

education

Requirements
Must have
• .the " 98% employment rate" should stand out in the ad.. but should not be the main part of the ad
Nice to have
• creative
Should not have
• Should not be a very busy or crowded ad.. i prefer pictures of men but should be .. in a business suit .. that looks professional- white shirt

```html
<!DOCTYPE html>
<html lang="en">
<head>
<meta charset="utf-8">
<title>HRU Masters of Accounting – Ad Variants</title>
<link href="https://fonts.googleapis.com/css2?family=Inter+Tight:wght@800;900&family=Questrial&family=Archivo:wght@800&display=swap" rel="stylesheet">
<style>
  :root {
    --stage: #e9e9ea;
    --panel: #1c1c1c;
    --ink: #111111;
    --white: #ffffff;
    --pill: #ececec;
    --accent: #ffffff;
    --cyan: #4cc4dc;
  }
  * { margin: 0; padding: 0; box-sizing: border-box; }
  html, body { width: 1200px; height: 790px; overflow: hidden; background: var(--stage); }
  .stage { position: relative; width: 1200px; height: 790px; }

  .flyer {
    position: absolute; top: 61px; width: 492px; height: 659px;
    background: var(--panel); overflow: hidden;
    box-shadow: 0 14px 18px -10px rgba(0,0,0,.35);
  }
  .flyer--mono { left: 61px; }
  .flyer--color { left: 641px; --accent: var(--cyan); }

  .hero { position: absolute; left: 0; top: 0; width: 492px; height: 346px; }
  .flyer--mono .hero {
    background:
      radial-gradient(ellipse 55% 70% at 78% 55%, #3a3a3a 0%, #5a5a5a 45%, rgba(255,255,255,0) 75%),
      linear-gradient(90deg, #f4f4f4 0%, #dcdcdc 45%, #bdbdbd 70%, #e2e2e2 100%);
  }
  .flyer--color .hero {
    background:
      radial-gradient(ellipse 50% 70% at 80% 58%, #1d5fb0 0%, #2f77c4 40%, rgba(255,255,255,0) 75%),
      linear-gradient(90deg, #f2f7fb 0%, #d6e6f1 45%, #a9c6dc 70%, #dfeaf3 100%);
  }

  .headline { position: absolute; left: 40px; top: 56px; color: var(--ink); line-height: 1; }
  .headline .line { display: block; white-space: nowrap; }
  .headline .lead { font-family: 'Questrial', sans-serif; font-size: 27px; margin-right: 4px; }
  .headline .heavy { font-family: 'Inter Tight', sans-serif; font-weight: 900; letter-spacing: -1.6px; }
  .headline .light { font-family: 'Questrial', sans-serif; font-size: 35px; letter-spacing: -1.6px; line-height: .86; }
  .headline .big-1 { font-size: 44px; line-height: .9; }
  .headline .big-2 { font-size: 56px; line-height: .84; }
  .headline .mid { font-size: 32px; line-height: .9; }
  .headline .gap { margin-top: 12px; }

  .facts { position: absolute; left: 0; top: 346px; width: 492px; height: 313px; color: var(--white); }

  .program-badge {
    position: absolute; left: 42px; top: 30px; width: 176px; height: 38px;
    background: var(--pill); border-radius: 8px; color: var(--ink);
    display: flex; align-items: center; gap: 8px; padding-left: 13px;
  }
  .program-badge .name { font-family: 'Archivo', sans-serif; font-weight: 800; font-size: 26px; letter-spacing: -.5px; }
  .program-badge .title { font-family: 'Questrial', sans-serif; font-size: 14px; line-height: .88; letter-spacing: .3px; }

  .divider-v { position: absolute; width: 1.5px; background: var(--white); }
  .divider-v--top { left: 251px; top: 30px; height: 38px; }

  .stat { position: absolute; left: 275px; top: 32px; display: flex; align-items: center; gap: 5px; }
  .stat .value { font-family: 'Archivo', sans-serif; font-weight: 800; font-size: 33px; letter-spacing: -1.5px; color: var(--accent); }
  .stat .label { font-family: 'Questrial', sans-serif; font-size: 15px; letter-spacing: 3px; line-height: .9; }

  .feature { position: absolute; top: 87px; display: flex; gap: 10px; }
  .feature--jobs { left: 42px; }
  .feature--salary { left: 224px; }
  .feature .icon {
    width: 32px; height: 32px; border-radius: 50%;
    background: #4b4b4b; border: 1.5px solid #777; flex: none; margin-top: 1px;
    display: flex; align-items: center; justify-content: center;
  }
  .feature p { font-family: 'Questrial', sans-serif; font-size: 12px; line-height: 12.3px; color: #eee; }

  .rankings {
    position: absolute; left: 42px; top: 172px; width: 420px; height: 73px;
    border: 1.3px solid var(--accent); border-radius: 12px;
  }
  .rankings .tag {
    position: absolute; left: 38px; top: -22px; background: var(--panel);
    display: flex; align-items: flex-end; gap: 6px; padding: 0 4px;
  }
  .rankings .tag span { font-family: 'Questrial', sans-serif; font-size: 11.5px; line-height: 10px; color: var(--white); padding-bottom: 3px; }
  .rankings .col { position: absolute; top: 24px; white-space: nowrap; }
  .rankings .col--a { left: 20px; width: 122px; }
  .rankings .col--b { left: 164px; width: 240px; }
  .rankings .divider-v { left: 149px; top: 24px; height: 40px; }
  .rankings h3 { font-family: 'Archivo', sans-serif; font-weight: 800; font-size: 16.5px; line-height: 18px; color: var(--accent); }
  .rankings .source { font-family: 'Questrial', sans-serif; font-size: 16px; line-height: 18px; color: var(--white); }
</style>
</head>
<body>
<main class="stage">

  <article class="flyer flyer--mono">
    <div class="hero" role="img" aria-label="Black and white photo of a thoughtful businessman in a suit, white shirt and tie, working at a laptop in a bright office"></div>
    <h1 class="headline">
      <span class="line"><span class="lead">A</span><span class="heavy big-1">SMALL</span></span>
      <span class="line heavy mid">INVESTMENT</span>
      <span class="line light">TODAY</span>
      <span class="line gap"><span class="lead">A</span><span class="heavy big-2">BIG</span></span>
      <span class="line heavy mid">DIFFERENCE</span>
      <span class="line light">TOMORROW</span>
    </h1>
    <section class="facts">
      <div class="program-badge"><span class="name">HRU</span><span class="title">MASTERS OF<br>ACCOUNTING</span></div>
      <div class="divider-v divider-v--top"></div>
      <div class="stat"><span class="value">98%</span><span class="label">EMPLOYMENT<br>RATE</span></div>
      <div class="feature feature--jobs">
        <span class="icon"><svg width="16" height="16" viewBox="0 0 16 16" fill="none" stroke="#fff" stroke-width="1.4"><circle cx="7" cy="3" r="2"/><circle cx="7" cy="10" r="3.5"/><line x1="9.5" y1="12.5" x2="13" y2="15.5"/></svg></span>
        <p>HRU Graduates have<br>gone on to Work in<br>Various High-quality<br>Jobs in Top Firms</p>
      </div>
      <div class="feature feature--salary">
        <span class="icon"><svg width="16" height="16" viewBox="0 0 16 16" fill="none" stroke="#fff" stroke-width="1.3"><circle cx="9" cy="4.5" r="3.5"/><path d="M1 11l3-2h4l3 1M4 13h6l4-4"/></svg></span>
        <p>Earning Impressive<br>Six-figure Salaries as<br>Well as Opening<br>Successful Businesses.</p>
      </div>
      <div class="rankings">
        <div class="tag">
          <svg width="36" height="38" viewBox="0 0 36 38" fill="none" stroke="#fff" stroke-width="1.3"><path d="M14 1l1.3 2.7 3 .4-2.2 2 .6 3-2.7-1.5-2.7 1.5.6-3-2.2-2 3-.4z"/><rect x="3" y="26" width="6" height="10"/><rect x="11" y="14" width="6" height="22"/><rect x="19" y="22" width="6" height="14"/><rect x="27" y="18" width="6" height="18"/><line x1="0" y1="36" x2="36" y2="36"/></svg>
          <span>RANKED<br>AMONGST</span>
        </div>
        <div class="col col--a"><h3>Best Colleges</h3><p class="source">Corvane 2023</p></div>
        <div class="divider-v"></div>
        <div class="col col--b"><h3>Best Masters in Accounting</h3><p class="source">Academia Index 2023</p></div>
      </div>
    </section>
  </article>

  <article class="flyer flyer--color">
    <div class="hero" role="img" aria-label="Colour photo of a thoughtful businessman in a blue jacket, white shirt and tie, working at a laptop in a bright office"></div>
    <h1 class="headline">
      <span class="line"><span class="lead">A</span><span class="heavy big-1">SMALL</span></span>
      <span class="line heavy mid">INVESTMENT</span>
      <span class="line light">TODAY</span>
      <span class="line gap"><span class="lead">A</span><span class="heavy big-2">BIG</span></span>
      <span class="line heavy mid">DIFFERENCE</span>
      <span class="line light">TOMORROW</span>
    </h1>
    <section class="facts">
      <div class="program-badge"><span class="name">HRU</span><span class="title">MASTERS OF<br>ACCOUNTING</span></div>
      <div class="divider-v divider-v--top"></div>
      <div class="stat"><span class="value">98%</span><span class="label">EMPLOYMENT<br>RATE</span></div>
      <div class="feature feature--jobs">
        <span class="icon"><svg width="16" height="16" viewBox="0 0 16 16" fill="none" stroke="#fff" stroke-width="1.4"><circle cx="7" cy="3" r="2"/><circle cx="7" cy="10" r="3.5"/><line x1="9.5" y1="12.5" x2="13" y2="15.5"/></svg></span>
        <p>HRU Graduates have<br>gone on to Work in<br>Various High-quality<br>Jobs in Top Firms</p>
      </div>
      <div class="feature feature--salary">
        <span class="icon"><svg width="16" height="16" viewBox="0 0 16 16" fill="none" stroke="#fff" stroke-width="1.3"><circle cx="9" cy="4.5" r="3.5"/><path d="M1 11l3-2h4l3 1M4 13h6l4-4"/></svg></span>
        <p>Earning Impressive<br>Six-figure Salaries as<br>Well as Opening<br>Successful Businesses.</p>
      </div>
      <div class="rankings">
        <div class="tag">
          <svg width="36" height="38" viewBox="0 0 36 38" fill="none" stroke="#fff" stroke-width="1.3"><path d="M14 1l1.3 2.7 3 .4-2.2 2 .6 3-2.7-1.5-2.7 1.5.6-3-2.2-2 3-.4z"/><rect x="3" y="26" width="6" height="10"/><rect x="11" y="14" width="6" height="22"/><rect x="19" y="22" width="6" height="14"/><rect x="27" y="18" width="6" height="18"/><line x1="0" y1="36" x2="36" y2="36"/></svg>
          <span>RANKED<br>AMONGST</span>
        </div>
        <div class="col col--a"><h3>Best Colleges</h3><p class="source">Corvane 2023</p></div>
        <div class="divider-v"></div>
        <div class="col col--b"><h3>Best Masters in Accounting</h3><p class="source">Academia Index 2023</p></div>
      </div>
    </section>
  </article>

</main>
</body>
</html>
```